BOR Business Card

I need a business card to go with my new logo

Needs to have the following

Gareth Mulvey
gmulvey@copperhaven-studio.example
+61407553118
Twitter : @CopperHavenPix
http://copperhaven-studio.example
Facebook : www.friendwall.example/copperhavenreels
Youtube: http://www.videohub.example/user/Copperhaven

I would also want to have QR Code that points to the website.

The logo must be on the card on side.

At the end this need to be in a template that I can change the names or websites on as my business grows.
Updates

guys and girls i have uploaded the designs that need to be used here. one is for films and on is for foto so please make sure that these are used.

Target Market(s)

Parents and children who attend sporting events and would like there photos taken.

It also need to encompass family for portraits photography as well.

Industry/Entity Type

Business

Requirements
Must have
• Must have my logo on the card and must have the right colour balance

```html
<!DOCTYPE html>
<html lang="en">
<head>
<meta charset="utf-8">
<title>BOR Business Card</title>
<link rel="stylesheet" href="https://fonts.googleapis.com/css2?family=Open+Sans:wght@400;600;700&display=swap">
<style>
  :root {
    --stage: #1e1e1e;
    --stage-edge: #0c0c0c;
    --brand-red: #e3141c;
    --brand-red-deep: #b10d12;
    --card-white: #ffffff;
    --ink: #1f1f1f;
    --soft-white: rgba(255,255,255,0.92);
  }
  * { margin: 0; padding: 0; box-sizing: border-box; }
  html, body { width: 1200px; height: 871px; overflow: hidden; }
  body {
    background: radial-gradient(ellipse at 50% 40%, var(--stage) 0%, var(--stage-edge) 100%);
    font-family: "Open Sans", Arial, sans-serif;
    position: relative;
  }
  .card {
    position: absolute;
    top: 281px;
    width: 540px;
    height: 309px;
    border-radius: 22px;
    overflow: hidden;
    box-shadow: 0 12px 30px rgba(0,0,0,0.55);
  }
  .card--back {
    left: 40px;
    background: linear-gradient(135deg, var(--brand-red) 0%, var(--brand-red-deep) 100%);
    color: var(--soft-white);
    text-align: center;
  }
  .card--front {
    left: 620px;
    background: var(--card-white);
    color: var(--ink);
  }

  /* Wordmark */
  .wordmark { display: flex; flex-direction: column; align-items: center; }
  .wordmark__row { display: flex; align-items: center; gap: 10px; }
  .wordmark__initials { font-weight: 700; line-height: 1; letter-spacing: 1px; }
  .wordmark__dot { border-radius: 50%; }
  .wordmark__name { font-weight: 600; text-transform: uppercase; letter-spacing: 0.5px; white-space: nowrap; }

  .card--back .wordmark { margin-top: 48px; }
  .card--back .wordmark__initials { font-size: 74px; color: var(--card-white); }
  .card--back .wordmark__dot { width: 18px; height: 18px; background: var(--card-white); }
  .card--back .wordmark__name { font-size: 17px; color: var(--card-white); margin-top: 6px; }

  .social-list { list-style: none; margin-top: 22px; font-size: 9.5px; letter-spacing: 1px; line-height: 1.75; }

  /* Front */
  .holder {
    position: absolute; left: 38px; top: 66px;
    font-size: 13px; font-weight: 700; letter-spacing: 2.5px; color: var(--brand-red);
  }
  .contact-list { position: absolute; left: 38px; top: 134px; list-style: none; }
  .contact-list li { display: flex; font-size: 11px; letter-spacing: 1px; line-height: 25px; white-space: nowrap; }
  .contact-list .label { width: 22px; color: var(--brand-red); font-weight: 700; font-size: 10px; }

  .card--front .wordmark { position: absolute; right: 36px; top: 40px; }
  .card--front .wordmark__initials { font-size: 60px; color: var(--brand-red); }
  .card--front .wordmark__dot { width: 15px; height: 15px; background: var(--brand-red); }
  .card--front .wordmark__name { font-size: 14px; color: var(--brand-red); margin-top: 6px; }

  .band {
    position: absolute; left: 0; right: 0; bottom: 0; height: 66px;
    background: linear-gradient(90deg, var(--brand-red) 0%, var(--brand-red-deep) 100%);
  }
  .band__mark {
    position: absolute; left: 252px; top: 16px;
    width: 24px; height: 24px; border-radius: 50%; background: var(--card-white);
  }
</style>
</head>
<body>
  <section class="card card--back" aria-label="Card back">
    <div class="wordmark">
      <div class="wordmark__row">
        <span class="wordmark__initials">BOR</span>
        <span class="wordmark__dot"></span>
      </div>
      <span class="wordmark__name">Copperhaven Films</span>
    </div>
    <ul class="social-list">
      <li>@CopperHavenPix</li>
      <li>www.friendwall.example/copperhavenreels</li>
      <li>http://www.videohub.example/user/Copperhaven</li>
    </ul>
  </section>

  <section class="card card--front" aria-label="Card front">
    <p class="holder">Gareth Mulvey</p>
    <ul class="contact-list">
      <li><span class="label">E</span><span>gmulvey@copperhaven-studio.example</span></li>
      <li><span class="label">P</span><span>+61407553118</span></li>
      <li><span class="label">W</span><span>copperhaven-studio.example</span></li>
    </ul>
    <div class="wordmark">
      <div class="wordmark__row">
        <span class="wordmark__initials">BOR</span>
        <span class="wordmark__dot"></span>
      </div>
      <span class="wordmark__name">Copperhaven Films</span>
    </div>
    <div class="band">
      <span class="band__mark"></span>
    </div>
  </section>
</body>
</html>
```